Copper Vale Tattoo

Business card / Appointment card in one

Ive attached the new logo along with a simple format of what I would like written out on the back! Would like a clean/ modern style font to be used! I also attached the current card for a reference of style!

The colors of this would be either white and gold lettering or black with gold lettering.

Email - CopperValeNB@inkmail.example
Ph # 555-482-9073

The message at bottom of back - All cancellations or No Call No Shows within 48 hours of appointment time will result in a forfeit of deposit.

Small block avail (if card is black) to write in appointment date/time

Target Market(s)

Card for Tattoo shop

Contact Information for Business Card

in project description area!

Font styles to use
Sans Serif

Requirements
Must have
• Please refer to current business card photos that were attached as well!
Nice to have
• Looking for blacks, greys and gold for color scheme

```html
<!DOCTYPE html>
<html lang="en">
<head>
<meta charset="utf-8">
<title>Copper Vale Tattoo – Business &amp; Appointment Card</title>
<link href="https://fonts.googleapis.com/css2?family=Lato:wght@400;700&family=Oswald:wght@400&display=swap" rel="stylesheet">
<style>
  :root {
    --page-bg: #2b2b2b;
    --card-bg: #3b3b3d;
    --gold: #cfa95e;
    --gold-soft: #bf9d5a;
    --rule: #8a7a5a;
    --band: #d5d5d5;
    --band-text: #a9a9a9;
    --band-line: #9c9c9c;
  }
  * { box-sizing: border-box; margin: 0; padding: 0; }
  html, body {
    width: 1200px;
    height: 1108px;
    overflow: hidden;
    background: var(--page-bg);
  }
  .card-set {
    position: relative;
    width: 1200px;
    height: 1108px;
  }
  .card {
    position: absolute;
    top: 224px;
    width: 420px;
    height: 660px;
    border-radius: 28px;
    background: var(--card-bg);
    overflow: hidden;
    box-shadow: 0 10px 30px rgba(0,0,0,0.45);
  }
  .card--front { left: 150px; }
  .card--back { left: 630px; }

  /* Front */
  .brand-mark {
    position: absolute;
    inset: 0;
    display: flex;
    align-items: center;
    justify-content: center;
    gap: 14px;
  }
  .brand-mark__square {
    width: 22px;
    height: 22px;
    border: 3px solid var(--gold);
  }
  .brand-mark__name {
    font-family: "Lato", sans-serif;
    font-weight: 700;
    font-size: 32px;
    color: var(--gold);
    letter-spacing: 0.5px;
  }

  /* Back */
  .shop-name {
    position: absolute;
    top: 66px;
    width: 100%;
    text-align: center;
    font-family: "Lato", sans-serif;
    font-weight: 400;
    font-size: 38px;
    line-height: 48px;
    letter-spacing: 0.5px;
    color: var(--gold);
  }
  .divider {
    position: absolute;
    left: 120px;
    width: 180px;
    height: 1px;
    background: var(--rule);
  }
  .divider--top { top: 150px; }
  .divider--mid { top: 318px; }
  .contact {
    position: absolute;
    top: 184px;
    width: 100%;
    text-align: center;
    font-family: "Oswald", sans-serif;
    font-size: 27px;
    line-height: 42px;
    color: var(--gold);
  }
  .policy {
    position: absolute;
    top: 346px;
    left: 20px;
    right: 20px;
    text-align: center;
    font-family: "Lato", sans-serif;
    font-size: 18px;
    line-height: 24px;
    color: var(--gold-soft);
  }
  .appointment-band {
    position: absolute;
    top: 470px;
    left: 0;
    width: 100%;
    height: 132px;
    background: var(--band);
  }
  .appointment-band__label {
    position: absolute;
    top: 40px;
    width: 100%;
    text-align: center;
    font-family: "Lato", sans-serif;
    font-size: 17px;
    color: var(--band-text);
  }
  .appointment-band__line {
    position: absolute;
    top: 100px;
    left: 60px;
    right: 60px;
    height: 1px;
    background: var(--band-line);
  }
</style>
</head>
<body>
  <main class="card-set">
    <section class="card card--front" aria-label="Card front">
      <div class="brand-mark">
        <span class="brand-mark__square"></span>
        <span class="brand-mark__name">Copper Vale Tattoo</span>
      </div>
    </section>

    <section class="card card--back" aria-label="Card back">
      <h1 class="shop-name">Copper Vale Tattoo</h1>
      <div class="divider divider--top"></div>
      <p class="contact">555-482-9073<br>CopperValeNB@inkmail.example</p>
      <div class="divider divider--mid"></div>
      <p class="policy">All cancellations or No Call No Shows<br>within 48 hours of appointment time<br>will result in a forfeit of deposit.</p>
      <div class="appointment-band">
        <span class="appointment-band__label">Date &amp; Time</span>
        <span class="appointment-band__line"></span>
      </div>
    </section>
  </main>
</body>
</html>
```